San Francisco Leading Consulting firm - 47Nova Web Design Project

•Create a Web Design
•Uncoded webpage layout design
•2 Pages Design - Homepage + Interior Page

Task Description
Hello, we're looking for a re-design our current website www.47nova-example.com

we have a sample mockup design @

http://47nova.civicpane-example.org/

This shows the layout that we like and also a sample of 6 pictures that would change based on where you mouse over..

6 pictures HOME design needs to be included.

SMART
THOUGHTFUL
FLEXIBLE
CREATIVE SERVICES
TECHNICAL SERVICES
PARTNERS

sites we like:

http://www.brelmoradvisory-example.com/Home.cfm?id=Home
http://www.pixelquarry-example.com/index.html

Our company can be best described as: 100+ employees, cutting-edge, depandable, innovative, strong, smart.

Our Primary focus is: IT Consulting Services and Creative Design services

47Nova LLC is a consulting firm providing creative design, business and technology solutions to both private and public interests.

Established in 1996, 47Nova is a San Francisco based company providing specialists for a range of business needs including:

Creative Design Services
•Print
•Logo Design
•Website Design
•Illustration

and

Business and Technology solutions

•Application Software and Web Development
•Business Process Re-Design (BPR)
•Business/Systems Analysis and Requirement Documentation
•Mentoring and Training
•Network/Hardware Installation Services
•System Design and Architecture
•Vendor Management
•Teamvault Architecture and Implementation

our sample mockup site:

Reason: Due to holiday season, we're not available to work with designers and finilize our design.  

Thank you very much for submitting your design.

We appreciate your time and creativity.   Since, our office is currently closed for holidays, we will be reviewing it in details next week and will make our decision as soon as possible.

It would be great if you could submit any of your changes by Wed next week, so it would be part of our reviews. 

Please see updated wireframe under attachments:  we have some minor updates to our wireframe that we would like you to update your designs, if possible.  

We also encorouge you not to use our standard wireframe and come up with more unique designs.   Everything would be considered when we review your design.

 

Target Market(s)

Creative services and professional services clients, including government agencies

Industry/Entity Type

Business

Requirements
Must have
• Clean, professional look, easy navigation

```html
<!DOCTYPE html>
<html lang="en">
<head>
<meta charset="utf-8">
<title>47Nova — Business and Technology Consulting</title>
<link rel="stylesheet" href="https://fonts.googleapis.com/css2?family=Open+Sans:wght@300;400;600;700&display=swap">
<style>
  :root{
    --page-bg:#ffffff;
    --frame-line:#c9c9c9;
    --header-dark:#243434;
    --header-mid:#3c5252;
    --tab-green:#dfe7a6;
    --tab-green-dark:#c9d48a;
    --tab-border:#b5c177;
    --banner-light:#eef2c4;
    --banner-mid:#d9e29c;
    --banner-band:#b6bf83;
    --ink:#222222;
    --ink-soft:#333333;
    --heading-olive:#4b4f37;
    --link-blue:#1f4fa8;
    --rss-orange:#e4561c;
    --footer-teal:#0d7f80;
    --footer-teal-dark:#075b5c;
    --footer-cap:#9a9a9a;
    --input-bg:#f4f4f4;
    --art-green:#9cc08a;
    --art-amber:#e3c690;
    --art-red:#dd9c90;
  }
  *{box-sizing:border-box;margin:0;padding:0}
  html,body{width:1200px;height:900px;overflow:hidden;background:var(--page-bg)}
  body{font-family:"Open Sans",Verdana,sans-serif;color:var(--ink)}
  .canvas{position:relative;width:1200px;height:900px;overflow:hidden}

  .page-frame{position:absolute;left:142px;top:0;width:918px;height:900px;
    border-left:1px solid var(--frame-line);border-right:1px solid var(--frame-line)}
  .header-band{position:absolute;left:143px;top:0;width:916px;height:222px;
    background:linear-gradient(180deg,var(--header-dark) 0%,var(--header-mid) 100%)}

  .brand{position:absolute;left:207px;top:0;width:180px;height:93px;background:#fff;
    border:1px solid var(--frame-line);border-top:none;display:flex;align-items:center;gap:10px;padding-left:18px}
  .brand-mark{width:26px;height:26px;background:#7fb535}
  .brand-name{font-size:30px;font-weight:400;color:#3a3a3a;letter-spacing:0.5px}

  .search{position:absolute;left:798px;top:60px;display:flex;align-items:center;gap:8px}
  .search-label{color:#fff;font-size:12px}
  .search-field{width:180px;height:17px;border-radius:9px;background:var(--input-bg);position:relative}
  .search-go{position:absolute;right:0;top:0;width:17px;height:17px;border-radius:50%;background:#8db03a}
  .search-go svg{position:absolute;left:5px;top:4px}

  .main-panel{position:absolute;left:187px;top:93px;width:830px;height:740px;background:#fff;
    border-radius:14px 14px 0 0}

  .nav{position:absolute;left:234px;top:96px;height:48px;display:flex;gap:3px}
  .nav-tab{height:48px;background:linear-gradient(180deg,#e9efb9 0%,var(--tab-green) 60%,var(--tab-green-dark) 100%);
    border:1px solid var(--tab-border);border-bottom:none;border-radius:5px 5px 0 0;
    font-size:12px;color:#2b2b2b;display:flex;align-items:center;justify-content:center;white-space:nowrap}

  .rss-tab{position:absolute;left:1018px;top:138px;width:23px;height:54px;background:var(--rss-orange);
    color:#fff;font-size:10px;font-weight:700;border-radius:0 4px 4px 0;
    display:flex;align-items:center;justify-content:center}
  .rss-tab span{transform:rotate(-90deg)}

  .banner{position:absolute;left:193px;top:145px;width:818px;height:200px;border-radius:0 0 10px 10px;overflow:hidden;
    background:linear-gradient(90deg,var(--banner-mid) 0%,var(--banner-light) 60%,var(--banner-mid) 100%)}
  .banner-band{position:absolute;left:0;bottom:8px;width:100%;height:38px;background:var(--banner-band)}
  .banner-art{position:absolute;left:17px;top:40px;width:300px;height:118px;border-radius:4px;
    background:linear-gradient(90deg,var(--art-green) 0%,var(--art-amber) 50%,var(--art-red) 100%)}
  .banner-title{position:absolute;left:359px;top:26px;color:var(--heading-olive);font-weight:300;line-height:1}
  .banner-title .lead{display:block;font-size:27px;letter-spacing:-0.5px}
  .banner-title .name{display:block;font-size:33px;margin-left:70px;margin-top:2px}
  .banner-intro{position:absolute;left:361px;top:98px;width:300px;font-size:11px;line-height:15px;color:#333;letter-spacing:-0.1px}
  .banner-seal{position:absolute;left:650px;top:12px;width:126px;height:126px;border-radius:50%;
    background:radial-gradient(circle,#c9cf9c 0%,#dfe4b5 45%,rgba(230,234,190,0) 72%)}

  .sidebar{position:absolute;left:187px;top:352px;width:214px;height:430px;
    border:1px solid var(--frame-line);border-top:none;border-radius:0 0 12px 12px;padding:8px 0 0 16px}
  .sidebar-title{font-size:18px;font-weight:700;color:#1d1d1d;margin-bottom:7px}
  .quick-links{list-style:none;font-size:11px;line-height:16.5px;color:#1d1d1d}
  .more-link{display:block;margin-top:11px;font-size:11px;color:var(--link-blue);text-decoration:underline}

  .content{position:absolute;left:401px;top:352px;width:606px;height:430px;padding:18px 0 0 24px;
    background:linear-gradient(160deg,#ffffff 40%,#eeeeee 100%)}
  .content-title{font-size:17px;font-weight:700;color:#1d1d1d;margin-bottom:16px}
  .content p{font-size:11px;line-height:13px;color:var(--ink-soft);margin-bottom:13px;width:560px;letter-spacing:-0.1px}
  .content p.spaced{margin-top:30px}
  .service-list{list-style:none;font-size:11px;line-height:13px;color:var(--ink-soft);margin-left:16px;margin-top:-3px}
  .service-list li::before{content:"* "}

  .rule{position:absolute;left:143px;top:826px;width:916px;height:1px;background:var(--frame-line)}
  .footer-bar{position:absolute;left:357px;top:824px;width:491px;height:34px;border-radius:0 0 20px 20px;
    background:var(--footer-cap)}
  .footer-nav{position:absolute;left:384px;top:824px;width:437px;height:34px;
    background:linear-gradient(180deg,var(--footer-teal) 0%,var(--footer-teal-dark) 100%);
    display:flex;align-items:center;justify-content:center;font-size:9.5px;color:#fff;white-space:nowrap}
  .footer-nav span{padding:0 7px;border-left:1px solid rgba(255,255,255,0.7);line-height:12px}
  .footer-nav span:first-child{border-left:none}
  .copyright{position:absolute;left:0;top:880px;width:1200px;text-align:center;font-size:10px;color:#222}
</style>
</head>
<body>
<div class="canvas">
  <div class="page-frame"></div>
  <div class="header-band"></div>

  <div class="brand">
    <div class="brand-mark"></div>
    <div class="brand-name">47Nova</div>
  </div>

  <div class="search">
    <span class="search-label">Search</span>
    <div class="search-field">
      <div class="search-go">
        <svg width="8" height="9" viewBox="0 0 8 9"><path d="M0 0 L8 4.5 L0 9 Z" fill="#fff"/></svg>
      </div>
    </div>
  </div>

  <div class="main-panel"></div>

  <nav class="nav">
    <div class="nav-tab" style="width:73px">Home</div>
    <div class="nav-tab" style="width:120px">Government</div>
    <div class="nav-tab" style="width:102px">Corporate</div>
    <div class="nav-tab" style="width:102px">Clients</div>
    <div class="nav-tab" style="width:90px">Partners</div>
    <div class="nav-tab" style="width:140px">Testimonials</div>
    <div class="nav-tab" style="width:93px">Contact Us</div>
  </nav>

  <div class="rss-tab"><span>RSS</span></div>

  <section class="banner">
    <div class="banner-band"></div>
    <div class="banner-art" role="img" aria-label="Hero illustration of rising growth arrows"></div>
    <h1 class="banner-title"><span class="lead">Welcome to</span><span class="name">47 NOVA</span></h1>
    <p class="banner-intro">47Nova LLC is a consulting firm providing business and technology solutions to both private and public inter-</p>
    <div class="banner-seal" role="img" aria-label="Circular emblem decoration"></div>
  </section>

  <aside class="sidebar">
    <h2 class="sidebar-title">Quick Links</h2>
    <ul class="quick-links">
      <li>Accounting</li><li>Business Travel</li><li>Construction</li><li>Education</li>
      <li>Finance</li><li>Health Care</li><li>Industrial Goods</li><li>Internet</li>
      <li>Jobs</li><li>Legal</li><li>Management &amp; Strategy</li><li>Office Management</li>
      <li>Real Estate</li><li>Retail</li><li>Sales &amp; Marketing</li><li>Software</li>
      <li>Startup</li><li>Technology</li><li>Browse Directory</li>
    </ul>
    <a class="more-link">more resourses</a>
  </aside>

  <main class="content">
    <h2 class="content-title">Welcome to 47 Nova</h2>
    <p>47Nova LLC is a consulting firm providing business and technology solutions to both private and public inter-ests.</p>
    <p>Our experts possess broad industry knowledge which can help with technical and business process challenges, delivering solutions that are creative and cost effective.</p>
    <p class="spaced">Established in 1996, 47Nova is a San Francisco based company providing specialists for a range of business needs including:</p>
    <ul class="service-list">
      <li>Analysis</li>
      <li>Application Software and Web Development</li>
      <li>Business Process Re-Design (BPR)</li>
      <li>Business/Systems Analysis and Requirement Documentation</li>
      <li>Mentoring and Training</li>
      <li>Network/Hardware Installation Services</li>
      <li>Production Support</li>
      <li>Quality Assurance and Control (QA/QC)</li>
      <li>System Design and Architecture</li>
      <li>Vendor Management</li>
      <li>Teamvault Architecture and Implementation</li>
    </ul>
  </main>

  <div class="rule"></div>
  <div class="footer-bar"></div>
  <nav class="footer-nav">
    <span>Home</span><span>Government</span><span>Corporate</span><span>Testimonials</span><span>Clients &amp; Partners</span><span>Contact Us</span>
  </nav>
  <p class="copyright">Copyright © 2010 47Nova | All rights reserved.</p>
</div>
</body>
</html>
```